New Australian Beverage Company Needs a Bottle Label Design

We are after a bottle label design for our new aloe vera drinks called 'Bold Finch'.

There are 5+ different colourrs we would like to compliment the flavors.

We are after a logo that is simple and eye catching.
Updates

Target Market(s)

Our target market is open for all as we would like to supply our drinks to quench everyone's thirst, however our biggest customers would be the teenagers to adults up to around the age of 50.

Industry/Entity Type

It Company

Requirements
Must have
• We are after a refreshing label that catches the eyes and makes you feel like picking it up and drinking it.

```html
<!DOCTYPE html>
<html lang="en">
<head>
<meta charset="utf-8">
<title>Bold Finch Aloe Vera Drinks – Label</title>
<link rel="stylesheet" href="https://fonts.googleapis.com/css2?family=Poppins:wght@700&family=Didact+Gothic&family=Fredoka:wght@600&family=Arimo:wght@700&display=swap">
<style>
  :root{
    --stage:#000000;
    --sky:#ffffff;
    --sun:#fff200;
    --lime:#c3d82c;
    --leaf:#3fae3a;
    --leaf-light:#a8d65a;
    --leaf-mid:#6cbf3f;
    --leaf-dark:#1e7a2c;
    --splash:rgba(70,140,200,.28);
    --ink:#222222;
    --mark:#4fae3a;
    --flavor:#e32227;
    --white:#ffffff;
  }
  html,body{margin:0;padding:0;overflow:hidden;}
  body{width:1200px;height:1000px;background:var(--stage);position:relative;}
  .label{
    position:absolute;left:44px;top:130px;width:1112px;height:740px;overflow:hidden;
    background:linear-gradient(to bottom,var(--sky) 0%,var(--sky) 10%,#fffbb0 24%,var(--sun) 38%,#f0ef1e 50%,var(--lime) 63%,#8cc63f 80%,var(--leaf) 100%);
  }
  .splash{position:absolute;border-radius:50%;}
  .splash--left{left:-50px;top:-40px;width:150px;height:760px;
    background:radial-gradient(ellipse at center,var(--splash) 0%,rgba(70,140,200,0) 70%);}
  .splash--middle{left:400px;top:-60px;width:230px;height:700px;
    background:radial-gradient(ellipse at 50% 35%,var(--splash) 0%,rgba(70,140,200,0) 70%);}
  .splash--right{left:1000px;top:-40px;width:170px;height:800px;
    background:radial-gradient(ellipse at center,var(--splash) 0%,rgba(70,140,200,0) 70%);}
  .aloe-band{position:absolute;left:0;bottom:0;width:1112px;height:220px;display:block;}
  .panel{position:absolute;top:0;width:556px;height:740px;}
  .panel--a{left:0;}
  .panel--b{left:549px;}
  .brand-dot{
    position:absolute;left:70px;top:142px;width:116px;height:116px;border-radius:50%;
    background:var(--mark);
  }
  .brand-name{
    position:absolute;left:184px;top:50px;height:486px;
    writing-mode:vertical-rl;transform:rotate(180deg);
    font-family:'Poppins',sans-serif;font-weight:700;font-size:92px;line-height:84px;
    color:var(--ink);white-space:nowrap;text-align:right;
  }
  .product-title{
    position:absolute;left:294px;top:69px;margin:0;
    font-family:'Didact Gothic',sans-serif;font-weight:400;font-size:42px;line-height:55px;
    color:var(--ink);letter-spacing:0.5px;
  }
  .flavor-box{
    position:absolute;left:296px;top:242px;width:128px;height:250px;
    background:linear-gradient(to bottom,var(--white) 0%,var(--white) 30%,rgba(255,255,255,.45) 75%,rgba(255,255,255,0) 100%);
  }
  .flavor-label{
    margin:29px 0 0;text-align:center;
    font-family:'Arimo',sans-serif;font-weight:700;font-size:23px;color:var(--flavor);
  }
  .volume{
    position:absolute;left:294px;top:678px;margin:0;line-height:1;
    font-family:'Fredoka',sans-serif;font-weight:600;font-size:37px;color:var(--white);
    -webkit-text-stroke:6px #000;paint-order:stroke fill;
  }
</style>
</head>
<body>
  <div class="label">
    <div class="splash splash--left" role="img" aria-label="Water splash illustration"></div>
    <div class="splash splash--middle" role="img" aria-label="Water splash illustration"></div>
    <div class="splash splash--right" role="img" aria-label="Water splash illustration"></div>

    <svg class="aloe-band" viewBox="0 0 1112 220" role="img" aria-label="Illustration of green aloe vera leaves">
      <defs>
        <linearGradient id="aloeFill" x1="0" y1="0" x2="0" y2="1">
          <stop offset="0" stop-color="var(--leaf-light)"/>
          <stop offset="0.45" stop-color="var(--leaf-mid)"/>
          <stop offset="1" stop-color="var(--leaf-dark)"/>
        </linearGradient>
      </defs>
      <path fill="url(#aloeFill)" d="M0 70 C60 40 120 30 180 70 C240 110 300 60 360 80 C420 100 480 20 560 40 C640 60 700 110 760 90 C820 70 880 100 940 90 C1000 80 1050 30 1112 40 L1112 220 L0 220 Z"/>
    </svg>

    <section class="panel panel--a">
      <div class="brand-dot"></div>
      <div class="brand-name">Bold Finch</div>
      <h1 class="product-title">ALOE<br>VERA<br>DRINKS</h1>
      <div class="flavor-box"><p class="flavor-label">FLAVORS</p></div>
      <p class="volume">500 ml</p>
    </section>

    <section class="panel panel--b">
      <div class="brand-dot"></div>
      <div class="brand-name">Bold Finch</div>
      <h1 class="product-title">ALOE<br>VERA<br>DRINKS</h1>
      <div class="flavor-box"><p class="flavor-label">FLAVORS</p></div>
      <p class="volume">500 ml</p>
    </section>
  </div>
</body>
</html>
```